Liquor Label / Aguardiente

Label design for liquor bottle. Designers may submit multiple submissions.

Product Description:
Name: Viento de Plata™
Alcohol Category: Aguardiente (which in Spanish most closely translates to “burning water”) – aguardiente is derived from
cane sugar and is a general term for a type of alcoholic spirit in many Central and South America countries.
Taste: A smooth liquor with a comfortable yet spicy finish
Smell: Subtle aroma of spicy jalapeños
Liquid Color: Clear
Bottle Color: Clear
See link for reference - http://www.kelvostamp.com/sites/default/files/styles/uc_product_full/public/Pemrow_0.jpg?itok=9QmT2xLp
Closure: Bar top / cork
Bottle Shape/Size: height = 8.67in; diameter of base = 3.70in; diameter of neck = 0.85in

Label may consist of two separate parts (i.e. front and back, front and vertical side), or one continuous label.

Designer has complete freedom with color, font etc. unless otherwise stated below. The label MUST
contain (but is not limited only to) the following text exactly as written in quotes below:
- “Viento de Plata”
- “Aguardiente”
- “Cane Neutral Spirit with Natural Flavors”
- “35% Alc./Vol.”
- “750 ml”
- “Bottled by WP Spirits, LLC” and “Nashville, TN” - “Government Warning: (1) According to the Surgeon General, women should not drink alcoholic beverages during
pregnancy because of the risk of birth defects. (2) Consumption of alcoholic beverages impairs your ability to
drive a car or operate machinery, and may cause health problems.” (text in previous quotes must be in all
capitalized letters, text must be 2 MM in height and quote must be separated 2MM by all other text)
- Must be dedicated empty space for bar code (approximately 0.75in. height x 1.25in. length)

Target Market(s)

Label should have mass market appeal.
Age: 21 – 28 years old (primary target market is 21+ year old college students and recent graduates)
Target Market Gender: Both male and female, with emphasis on male
Consumption Focus: Spirit will be consumed typically as a shot, primarily at bars and secondarily off premise (label design will be critical for making our product highly visible behind a bar)
Marketing Theme: South American elements. The official Viento de Plata mascot is a llama and the incorporation and use of a llama somewhere (however large or small) on the bottle is encourage but by no means required.

Industry/Entity Type

Health

Requirements
Should not have
• Elements that may lead a potential consumer to believe the beverage is a craft liquor or an artisan brand. Please do not include images of peppers.

```html
<!DOCTYPE html>
<html lang="en">
<head>
<meta charset="utf-8">
<title>Viento de Plata – Aguardiente Label Set</title>
<link href="https://fonts.googleapis.com/css2?family=Cinzel:wght@600&family=Pinyon+Script&family=Cormorant+SC:wght@600&display=swap" rel="stylesheet">
<style>
  :root {
    --bg: #ffffff;
    --gold: #c9a54a;
    --gold-deep: #8a6a22;
    --black: #0d0d0d;
    --rust: #6e2614;
    --navy: #16466e;
    --teal: #2c5a55;
    --plum: #5a2a40;
    --olive: #8e9a3a;
    --white: #f4f1e8;
  }
  html, body {
    margin: 0;
    width: 1200px;
    height: 900px;
    overflow: hidden;
    background: var(--bg);
  }
  .label-set {
    position: relative;
    width: 1200px;
    height: 900px;
  }
  .label {
    position: absolute;
    top: 250px;
    height: 420px;
    overflow: visible;
  }
  .label--classic { left: 130px; width: 243px; }
  .label--script  { left: 494px; width: 199px; }
  .label--stacked { left: 811px; width: 221px; }

  .fill-gold  { fill: var(--gold); }
  .fill-black { fill: var(--black); }
  .fill-rust  { fill: var(--rust); }
  .fill-navy  { fill: var(--navy); }
  .fill-teal  { fill: var(--teal); }
  .fill-plum  { fill: var(--plum); }
  .dots { stroke: var(--gold); stroke-width: 2.4; stroke-dasharray: 0.1 5; stroke-linecap: round; fill: none; }

  .category {
    font-family: "Cormorant SC", serif;
    font-size: 9px;
    letter-spacing: 1px;
    fill: var(--white);
  }
  .name-caps {
    font-family: "Cinzel", serif;
    font-weight: 600;
    fill: var(--white);
  }
  .name-script {
    font-family: "Pinyon Script", cursive;
    fill: var(--white);
  }
  .descriptor {
    font-family: "Cormorant SC", serif;
    font-weight: 600;
    fill: var(--gold);
  }
</style>
</head>
<body>
<main class="label-set">

  <!-- Classic label: caps name, split red/blue panels -->
  <svg class="label label--classic" viewBox="0 0 220 380" aria-label="Viento de Plata label, classic version">
    <path class="fill-gold" d="M0,100 A110,100 0 0 1 220,100 Z"/>
    <path class="fill-rust" d="M7,100 A103,93 0 0 1 110,7 L110,100 Z"/>
    <path class="fill-navy" d="M110,7 A103,93 0 0 1 213,100 L110,100 Z"/>
    <path class="fill-black" d="M20,100 A90,80 0 0 1 200,100 Z"/>
    <path class="fill-gold" opacity="0.75" role="img" aria-label="Gold sunburst ornament" d="M32,100 A78,68 0 0 1 188,100 L160,100 A50,44 0 0 0 60,100 Z"/>
    <path id="arc-classic" d="M64,96 A46,42 0 0 1 156,96" fill="none"/>
    <text class="category"><textPath href="#arc-classic" startOffset="50%" text-anchor="middle">AGUARDIENTE</textPath></text>

    <rect class="fill-black" x="0" y="100" width="220" height="68"/>
    <line class="dots" x1="6" y1="108" x2="214" y2="108"/>
    <line class="dots" x1="6" y1="160" x2="214" y2="160"/>
    <text class="name-caps" x="110" y="142" font-size="20" text-anchor="middle">VIENTO <tspan font-size="13">DE</tspan> PLATA</text>

    <path class="fill-gold" d="M4,170 H216 V280 A106,98 0 0 1 4,280 Z"/>
    <path class="fill-black" d="M10,176 H210 V280 A100,92 0 0 1 10,280 Z"/>
    <rect class="fill-gold" x="10" y="176" width="200" height="7" opacity="0.8" role="img" aria-label="Gold zigzag border"/>
    <rect class="fill-rust" x="22" y="188" width="88" height="84"/>
    <rect class="fill-navy" x="110" y="188" width="88" height="84"/>
    <rect class="fill-gold" x="74" y="196" width="72" height="68" opacity="0.85" role="img" aria-label="Gold Andean fret cross emblem"/>
    <path id="arc-classic-low" d="M34,282 A76,66 0 0 0 186,282" fill="none"/>
    <text class="descriptor" font-size="11"><textPath href="#arc-classic-low" startOffset="50%" text-anchor="middle">Cane Neutral Spirit with Natural Flavors</textPath></text>
    <path class="fill-gold" opacity="0.6" role="img" aria-label="Gold triangle fringe" d="M16,290 A94,78 0 0 0 204,290 L198,290 A88,72 0 0 1 22,290 Z"/>
  </svg>

  <!-- Script label: pill shape -->
  <svg class="label label--script" viewBox="0 0 180 380" aria-label="Viento de Plata label, script version">
    <path class="fill-gold" d="M0,90 A90,90 0 0 1 180,90 V290 A90,90 0 0 1 0,290 Z"/>
    <path class="fill-navy" d="M6,90 A84,84 0 0 1 174,90 Z"/>
    <path class="fill-black" d="M18,90 A72,72 0 0 1 162,90 Z"/>
    <path class="fill-gold" opacity="0.75" role="img" aria-label="Gold sunburst ornament" d="M28,90 A62,62 0 0 1 152,90 L128,90 A38,38 0 0 0 52,90 Z"/>
    <path id="arc-script" d="M54,86 A36,34 0 0 1 126,86" fill="none"/>
    <text class="category"><textPath href="#arc-script" startOffset="50%" text-anchor="middle">AGUARDIENTE</textPath></text>

    <rect class="fill-black" x="6" y="90" width="168" height="84"/>
    <line class="dots" x1="10" y1="98" x2="170" y2="98"/>
    <line class="dots" x1="10" y1="166" x2="170" y2="166"/>
    <rect class="fill-teal" x="10" y="104" width="160" height="56" opacity="0.7" role="img" aria-label="Teal, plum and olive woven cross pattern"/>
    <text class="name-script" x="90" y="140" font-size="26" text-anchor="middle">Viento <tspan font-size="14">de</tspan> Plata</text>

    <path class="fill-black" d="M6,176 H174 V290 A84,84 0 0 1 6,290 Z"/>
    <path class="fill-navy" d="M14,184 H166 V290 A76,76 0 0 1 14,290 Z"/>
    <path class="fill-black" d="M26,184 H154 V290 A64,64 0 0 1 26,290 Z"/>
    <rect class="fill-gold" x="54" y="194" width="72" height="66" opacity="0.85" role="img" aria-label="Gold Andean fret cross emblem"/>
    <path id="arc-script-low" d="M34,282 A56,54 0 0 0 146,282" fill="none"/>
    <text class="descriptor" font-size="7.6"><textPath href="#arc-script-low" startOffset="50%" text-anchor="middle">Cane Neutral Spirit with Natural Flavors</textPath></text>
    <path class="fill-gold" opacity="0.6" role="img" aria-label="Gold triangle fringe" d="M12,296 A78,72 0 0 0 168,296 L162,296 A72,66 0 0 1 18,296 Z"/>
  </svg>

  <!-- Stacked label: small "de Plata" over large script name -->
  <svg class="label label--stacked" viewBox="0 0 200 380" aria-label="Viento de Plata label, stacked version">
    <path class="fill-black" d="M10,84 A90,78 0 0 1 190,84 V110 H10 Z"/>
    <path class="fill-gold" opacity="0.75" role="img" aria-label="Gold sunburst ornament" d="M30,82 A70,62 0 0 1 170,82 L144,82 A44,40 0 0 0 56,82 Z"/>
    <path id="arc-stacked" d="M62,78 A38,34 0 0 1 138,78" fill="none"/>
    <text class="category"><textPath href="#arc-stacked" startOffset="50%" text-anchor="middle">AGUARDIENTE</textPath></text>

    <rect class="fill-black" x="0" y="80" width="200" height="96"/>
    <line class="dots" x1="6" y1="88" x2="194" y2="88"/>
    <line class="dots" x1="6" y1="168" x2="194" y2="168"/>
    <rect class="fill-plum" x="6" y="94" width="188" height="68" opacity="0.6" role="img" aria-label="Plum, teal and navy woven cross pattern"/>
    <text class="name-script" x="140" y="118" font-size="14" text-anchor="middle">de Plata</text>
    <text class="name-script" x="100" y="150" font-size="34" text-anchor="middle">Viento</text>

    <path class="fill-gold" d="M8,180 H192 V280 A92,92 0 0 1 8,280 Z"/>
    <path class="fill-black" d="M13,185 H187 V280 A87,87 0 0 1 13,280 Z"/>
    <rect class="fill-gold" x="13" y="185" width="174" height="7" opacity="0.8" role="img" aria-label="Gold zigzag border"/>
    <rect class="fill-gold" x="64" y="200" width="72" height="66" opacity="0.8" role="img" aria-label="Olive and gold Andean fret cross emblem"/>
    <path id="arc-stacked-low" d="M30,270 A70,64 0 0 0 170,270" fill="none"/>
    <text class="descriptor" font-size="9.5"><textPath href="#arc-stacked-low" startOffset="50%" text-anchor="middle">Cane Neutral Spirit with Natural Flavors</textPath></text>
    <path class="fill-gold" opacity="0.6" role="img" aria-label="Gold triangle fringe" d="M22,290 A78,72 0 0 0 178,290 L172,290 A72,66 0 0 1 28,290 Z"/>
  </svg>

</main>
</body>
</html>
```